Wine Label Design

We are looking for a new label to add to our winery. This is to be named "Lindgrube" which is the German word for schoolhouse. Our tasting room is a one room school house built in 1887. I would like the label to be very simple and clean with a schoolhouse on the front. I would like to schoolhouse to be sketch style, not a cartoonish design. I have attached a photo of the schoolhouse that we pour from, this is what I would want the schoolhouse to resemble. I have also added a copy of our current "higher end" label so that you have an idea of our style. I would like the new label to be cohesive with our old label and look good next to each other on our shelves. Just as added clarification we do not want Harlen Vineyards on the new label - we want that replaced with Lindgrube. If you are unable to do a full label design we would also accept just the schoolhouse drawing design as well. Thank you.

Logo Text

Lindgrube

```html
<!DOCTYPE html>
<html lang="en">
<head>
<meta charset="utf-8">
<title>Lindgrube Dry Rosé Label</title>
<link rel="stylesheet" href="https://fonts.googleapis.com/css2?family=Cabin+Sketch&family=Playwrite+FR+Moderne:wght@200&family=Josefin+Sans:wght@300&display=swap">
<style>
  :root {
    --page: #ffffff;
    --label-ground: #261c0b;
    --frame-gold: #d8ac3c;
    --ink-white: #ffffff;
    --ink-gold: #e2b43a;
    --rule-grey: #c9c6c0;
  }
  html, body {
    margin: 0;
    padding: 0;
    width: 1200px;
    height: 1200px;
    overflow: hidden;
    background: var(--page);
  }
  .canvas {
    width: 1200px;
    height: 1200px;
    display: block;
  }
  .label-ground { fill: var(--label-ground); }
  .frame-line {
    fill: none;
    stroke: var(--frame-gold);
    stroke-width: 1.4;
  }
  .frame-line--soft { stroke-width: 0.9; opacity: 0.75; }
  .brand-name {
    font-family: "Cabin Sketch", cursive;
    font-weight: 400;
    font-size: 92px;
    letter-spacing: 6px;
    fill: var(--ink-white);
  }
  .vintage {
    font-family: "Josefin Sans", sans-serif;
    font-weight: 300;
    font-size: 27px;
    letter-spacing: 5px;
    fill: var(--ink-gold);
  }
  .rule {
    stroke: var(--rule-grey);
    stroke-width: 2;
  }
  .wine-style {
    font-family: "Playwrite FR Moderne", cursive;
    font-weight: 200;
    font-size: 64px;
    fill: var(--ink-white);
  }
  .region {
    font-family: "Playwrite FR Moderne", cursive;
    font-weight: 200;
    font-size: 24px;
    fill: var(--ink-gold);
  }
</style>
</head>
<body>
<svg class="canvas" viewBox="0 0 1200 1200" xmlns="http://www.w3.org/2000/svg">
  <g class="label">
    <path class="label-ground"
      d="M220 1034 L220 180 Q230 150 270 135 Q420 92 625 92 Q830 92 980 135 Q1020 150 1030 180 L1030 1034 Z"/>

    <g class="label-frame">
      <path class="frame-line"
        d="M244 1008 L244 192 Q250 172 285 160 Q430 120 625 120 Q820 120 965 160 Q1000 172 1004 192 L1004 1008 Z"/>
      <path class="frame-line frame-line--soft"
        d="M248 1004 L247 195 Q254 176 288 164 Q432 124 625 124 Q818 124 962 164 Q996 176 1000 195 L1001 1004 Z"/>
    </g>

    <text class="brand-name" x="640" y="430" text-anchor="middle">LINDGRUBE</text>

    <text class="vintage" x="624" y="618" text-anchor="middle">2017</text>
    <line class="rule" x1="334" y1="638" x2="944" y2="638"/>

    <text class="wine-style" x="612" y="738" text-anchor="middle">Dry Rose</text>
    <line class="rule" x1="334" y1="782" x2="944" y2="782"/>

    <text class="region" x="624" y="842" text-anchor="middle">Finger Lakes</text>
  </g>
</svg>
</body>
</html>
```